Corvath Holdings, LLC

We are a design build general contracting company.
We work with commercial accounts and private developers. We build retail spaces, restaurants and housing projects.
Im looking for a clean professional type of logo incorporating a roman flavor, think ionic columns and pedestals.
Two toned colorway.
I like unusual fonts and Im not afraid to do something bold with the logo.
Contact Information for Business Card
Marisol Brenkowitz
318-472-9051 corvathmb@mailvexo.com
Font styles to use
Decorative
Colors
Designer to choose colors to be used in the design.
Requirements
Should not have
- I don't like reds pinks.

```html
<!DOCTYPE html>
<html lang="en">
<head>
<meta charset="utf-8">
<title>Corvath Holdings, LLC — Business Card</title>
<link href="https://fonts.googleapis.com/css2?family=Arimo:wght@400;700&display=swap" rel="stylesheet">
<style>
  :root {
    --stage: #2b2b2b;
    --card-dark: #050505;
    --card-light: #ffffff;
    --gold: #c9a227;
    --ink: #111111;
    --paper-text: #ffffff;
    --rule: #555555;
  }
  * { box-sizing: border-box; margin: 0; padding: 0; }
  html, body {
    width: 1200px; height: 880px; overflow: hidden;
    background: var(--stage);
    font-family: "Arimo", Arial, sans-serif;
  }
  .stage {
    width: 1200px; height: 880px;
    display: flex; flex-direction: column;
    align-items: center; justify-content: center; gap: 56px;
  }
  .card {
    width: 620px; height: 354px;
    border-radius: 26px;
    position: relative;
    box-shadow: 0 14px 30px rgba(0,0,0,.45);
  }
  .card--front { background: var(--card-dark); display: flex; align-items: center; justify-content: center; }
  .card--back { background: var(--card-light); display: flex; align-items: center; padding: 0 44px; }

  .brand { display: flex; align-items: center; gap: 16px; }
  .brand__dot {
    width: 54px; height: 54px; border-radius: 50%;
    border: 5px solid var(--gold); flex: none;
  }
  .brand__name {
    font-weight: 700; font-size: 30px; line-height: 1.05;
    letter-spacing: .5px;
  }
  .card--front .brand__name { color: var(--paper-text); }
  .card--back .brand__name { color: var(--ink); }

  .divider { width: 1px; height: 96px; background: var(--rule); margin: 0 30px; flex: none; }

  .contact { color: var(--ink); }
  .contact__name { font-weight: 700; font-size: 19px; margin-bottom: 16px; }
  .contact__line { display: flex; align-items: center; gap: 8px; font-size: 15px; line-height: 1.45; }
  .contact__icon { width: 13px; height: 13px; flex: none; }
</style>
</head>
<body>
<main class="stage">
  <section class="card card--front" aria-label="Card front">
    <div class="brand">
      <span class="brand__dot"></span>
      <span class="brand__name">Corvath<br>Holdings, LLC</span>
    </div>
  </section>

  <section class="card card--back" aria-label="Card back">
    <div class="brand">
      <span class="brand__dot"></span>
      <span class="brand__name">Corvath<br>Holdings, LLC</span>
    </div>
    <span class="divider"></span>
    <div class="contact">
      <p class="contact__name">Marisol Brenkowitz</p>
      <p class="contact__line">
        <svg class="contact__icon" viewBox="0 0 14 14" aria-hidden="true">
          <rect x="3" y="1" width="8" height="12" rx="1.5" fill="none" stroke="#c9a227" stroke-width="1.6"/>
          <circle cx="7" cy="10.6" r=".9" fill="#c9a227"/>
        </svg>
        318-472-9051
      </p>
      <p class="contact__line">
        <svg class="contact__icon" viewBox="0 0 14 14" aria-hidden="true">
          <rect x="1" y="3" width="12" height="8" fill="#c9a227"/>
          <path d="M1 3 L7 8 L13 3" fill="none" stroke="#fff" stroke-width="1.2"/>
        </svg>
        corvathmb@mailvexo.com
      </p>
    </div>
  </section>
</main>
</body>
</html>
```